Need a PowerPoint that reflects the company brand has great graphics.

Want a PowerPoint for a financial advisory firm that has continuity. Our practice builds financial advisory plans for individuals. We have three sub divisions so I need some slides branded to reflect each. To better understand these requirements please visit our website at: http://lindenpr.kzqt4-rv7.b9servo.com

I want the colors of the logo to be the focal point throughout the slide designs. This needs to look extremely professional.

```html
<!DOCTYPE html>
<html lang="en">
<head>
<meta charset="utf-8">
<title>Linden Peak Wealth – Presentation Deck</title>
<link rel="stylesheet" href="https://fonts.googleapis.com/css2?family=Oswald:wght@500;700&family=Open+Sans:wght@400;600;700&display=swap">
<style>
:root{
  --navy:#2f3d5c;
  --navy-deep:#283552;
  --orange:#f7a035;
  --orange-soft:#fbc27c;
  --blue:#2e7fb8;
  --slate:#7b8399;
  --grey:#ececee;
  --grey-mid:#d9d9dd;
  --photo-warm:#a7a39b;
  --photo-cool:#8d949d;
  --ink:#333;
  --white:#fff;
}
*{box-sizing:border-box;margin:0;padding:0}
html,body{width:1200px;height:1000px;overflow:hidden;background:var(--white)}
body{position:relative;font-family:"Open Sans",Arial,sans-serif;color:var(--ink)}
.slide{position:absolute;width:364px;height:210px;overflow:hidden;background:var(--white)}
.slide>svg.bg{position:absolute;inset:0;width:100%;height:100%}
.abs{position:absolute}
.head{font-family:"Oswald",Impact,sans-serif;font-weight:700;text-transform:uppercase;letter-spacing:1px;line-height:1.05;color:var(--navy)}
.hl{color:var(--orange)}
.body{font-size:5.2px;line-height:1.45;color:#444}
.brand{display:flex;align-items:center;gap:4px;font-family:"Open Sans",Arial,sans-serif;font-weight:700;color:var(--navy);white-space:nowrap}
.brand i{display:block;background:var(--orange)}
.brand-sm{font-size:4px;gap:2px}
.brand-sm i{width:6px;height:6px}
.dots{display:flex;gap:4px}
.dots b{width:8px;height:8px;border-radius:50%;display:block}
.pill{border-radius:8px;text-align:center;font-weight:600}
.num{width:18px;height:18px;border-radius:50%;background:var(--navy);color:var(--white);font-family:"Oswald",sans-serif;font-weight:700;font-size:11px;display:flex;align-items:center;justify-content:center}
.toc-item{display:flex;gap:6px;width:140px}
.toc-item h4{font-size:6px;color:var(--navy);font-weight:700}
.toc-item p{font-size:4.8px;line-height:1.4;color:#444}
.member{width:64px;text-align:center}
.member .photo{width:60px;height:58px;margin:0 auto}
.member .pill{background:var(--orange);color:var(--navy);font-size:5px;padding:1px 0;margin:6px 5px 3px}
.service{width:74px;text-align:center}
.service h5{color:var(--orange);font-size:5.5px;font-weight:700;line-height:1.2;margin:5px 0 3px}
.service p{font-size:4px;line-height:1.4;color:#333}
table.data{border-collapse:collapse;width:180px;font-size:5.5px;color:#333}
table.data th{background:var(--orange);color:var(--white);font-family:"Oswald",sans-serif;font-weight:500;font-size:5px;padding:1.5px 4px}
table.data td{padding:1.5px 4px;text-align:center}
table.data tr:nth-child(odd) td{background:#f4f4f5}
table.data tr:nth-child(even) td{background:#d7d8dc}
table.data td:nth-child(2){text-align:left}
.contact h4{font-size:7px;font-weight:700;color:var(--navy)}
.contact a{font-size:6.5px;color:var(--blue);display:block;line-height:1.35}
</style>
</head>
<body>

<!-- Slide 1: title -->
<section class="slide" style="left:25px;top:63px">
  <svg class="bg" viewBox="0 0 364 210">
    <rect width="364" height="210" fill="var(--grey)"/>
    <polygon points="0,0 215,0 170,210 0,210" fill="var(--photo-warm)" role="img" aria-label="Photo of a person working on a laptop"/>
    <rect x="20" y="0" width="50" height="125" fill="var(--orange)" opacity=".85"/>
    <rect x="0" y="120" width="105" height="55" fill="var(--navy)" opacity=".92"/>
    <polygon points="0,196 240,196 230,210 0,210" fill="var(--blue)"/>
    <polygon points="260,196 364,196 364,210 252,210" fill="var(--orange)"/>
  </svg>
  <div class="abs brand" style="left:262px;top:32px;font-size:9px"><i style="width:12px;height:12px"></i>Linden Peak</div>
  <div class="abs dots" style="left:262px;top:90px">
    <b style="background:var(--navy)"></b><b style="background:var(--blue)"></b><b style="background:var(--blue)"></b><b style="background:var(--orange)"></b><b style="background:var(--orange)"></b><b style="background:var(--grey-mid)"></b>
  </div>
  <div class="abs head" style="right:20px;top:114px;font-size:14px;text-align:right">Your Awesome<br><span class="hl">Title Here</span></div>
  <div class="abs" style="right:20px;top:168px;font-size:6px;color:var(--navy)">Superior results demand a unique approach</div>
</section>

<!-- Slide 2: section title -->
<section class="slide" style="left:418px;top:63px">
  <svg class="bg" viewBox="0 0 364 210">
    <defs><linearGradient id="city" x1="0" y1="0" x2="0" y2="1"><stop offset="0" stop-color="#f4a650"/><stop offset="1" stop-color="#e99236"/></linearGradient></defs>
    <rect width="364" height="210" fill="url(#city)" role="img" aria-label="City skyline photo with orange overlay"/>
  </svg>
  <div class="abs brand" style="left:128px;top:36px;font-size:9px"><i style="width:12px;height:12px"></i>Linden Peak</div>
  <div class="abs head" style="left:0;width:364px;top:90px;font-size:15px;text-align:center">Your Title <span style="color:var(--white)">Here</span></div>
  <div class="abs" style="left:112px;width:140px;top:120px;font-size:5px;line-height:1.4;color:var(--white);text-align:center">Lorem ipsum dolor sit amet, quis te sint sanctus, et his vero zril reprimique. Eu eos inani percipit laboramus sed.</div>
  <div class="abs pill" style="left:131px;top:158px;width:100px;height:16px;line-height:16px;background:var(--navy);color:var(--white);font-size:6px">Lorem ipsum dolor sit amet</div>
</section>

<!-- Slide 3: contents -->
<section class="slide" style="left:811px;top:63px">
  <svg class="bg" viewBox="0 0 364 210">
    <rect width="364" height="210" fill="var(--white)"/>
    <polygon points="0,0 120,0 0,90" fill="var(--grey)"/>
    <polygon points="150,0 270,0 200,210 110,210" fill="#f5f5f6"/>
    <polygon points="150,0 290,0 325,210 180,210" fill="var(--orange-soft)"/>
    <line x1="188" y1="55" x2="188" y2="190" stroke="var(--navy)" stroke-width="1"/>
  </svg>
  <div class="abs brand brand-sm" style="left:15px;top:12px"><i></i>Linden Peak</div>
  <div class="abs head" style="right:14px;top:12px;font-size:17px">Contents</div>
  <div class="abs toc-item" style="left:18px;top:58px"><div class="num">1</div><div><h4>About Us</h4><p>Lorem ipsum dolor sit amet, qui te sint sanctus, et his vero zril reprimique. Eu eos inani percipit laboramus.</p></div></div>
  <div class="abs toc-item" style="left:18px;top:108px"><div class="num">2</div><div><h4>About Us</h4><p>Lorem ipsum dolor sit amet, qui te sint sanctus, et his vero zril reprimique. Eu eos inani percipit laboramus.</p></div></div>
  <div class="abs toc-item" style="left:18px;top:158px"><div class="num">3</div><div><h4>About Us</h4><p>Lorem ipsum dolor sit amet, qui te sint sanctus, et his vero zril reprimique. Eu eos inani percipit laboramus.</p></div></div>
  <div class="abs toc-item" style="left:196px;top:58px;width:160px"><div class="num">4</div><div><h4>About Us</h4><p>Lorem ipsum dolor sit amet, qui te sint sanctus, et his vero zril reprimique. Eu eos inani percipit laboramus.</p></div></div>
  <div class="abs toc-item" style="left:196px;top:108px;width:160px"><div class="num">5</div><div><h4>About Us</h4><p>Lorem ipsum dolor sit amet, qui te sint sanctus, et his vero zril reprimique. Eu eos inani percipit laboramus.</p></div></div>
  <div class="abs toc-item" style="left:196px;top:158px;width:160px"><div class="num">6</div><div><h4>About Us</h4><p>Lorem ipsum dolor sit amet, qui te sint sanctus, et his vero zril reprimique. Eu eos inani percipit laboramus.</p></div></div>
</section>

<!-- Slide 4: team -->
<section class="slide" style="left:25px;top:288px">
  <svg class="bg" viewBox="0 0 364 210">
    <rect width="364" height="210" fill="var(--grey)"/>
    <polygon points="0,80 80,210 0,210" fill="#e2e2e5"/>
    <polygon points="200,0 364,0 364,120" fill="#f3f3f4"/>
    <polygon points="250,210 364,90 364,210" fill="#dedee2"/>
  </svg>
  <div class="abs brand brand-sm" style="left:15px;top:12px"><i></i>Linden Peak</div>
  <div class="abs head" style="right:18px;top:20px;font-size:15px">Meet Our <span class="hl">Group</span></div>
  <div class="abs member" style="left:43px;top:60px">
    <svg class="photo" viewBox="0 0 60 58" role="img" aria-label="Portrait photo of team member"><rect width="60" height="58" fill="var(--photo-cool)"/><rect width="14" height="28" fill="var(--orange)" opacity=".8"/><rect x="40" y="36" width="20" height="22" fill="var(--navy)" opacity=".85"/></svg>
    <div class="pill">Name Here</div>
    <p class="body">Lorem ipsum dolor sit amet, quis te sint sanctus, et his vero zril reprimique. Eu eos inani percipit laboramus.</p>
  </div>
  <div class="abs member" style="left:153px;top:60px">
    <svg class="photo" viewBox="0 0 60 58" role="img" aria-label="Photo of team members in a meeting"><rect width="60" height="58" fill="var(--photo-warm)"/><rect x="8" width="16" height="30" fill="var(--navy)" opacity=".85"/><rect x="36" y="30" width="24" height="28" fill="var(--orange)" opacity=".8"/></svg>
    <div class="pill">Name Here</div>
    <p class="body">Lorem ipsum dolor sit amet, quis te sint sanctus, et his vero zril reprimique. Eu eos inani percipit laboramus.</p>
  </div>
  <div class="abs member" style="left:265px;top:60px">
    <svg class="photo" viewBox="0 0 60 58" role="img" aria-label="Portrait photo of team member"><rect width="60" height="58" fill="#b49e8e"/><rect x="40" width="20" height="26" fill="var(--orange)" opacity=".8"/><rect y="40" width="24" height="18" fill="var(--navy)" opacity=".85"/></svg>
    <div class="pill">Name Here</div>
    <p class="body">Lorem ipsum dolor sit amet, quis te sint sanctus, et his vero zril reprimique. Eu eos inani percipit laboramus.</p>
  </div>
</section>

<!-- Slide 5: about -->
<section class="slide" style="left:418px;top:288px">
  <svg class="bg" viewBox="0 0 364 210">
    <rect width="364" height="210" fill="var(--white)"/>
    <polygon points="0,0 140,0 0,130" fill="var(--grey)"/>
    <polygon points="150,0 225,0 190,210 100,210" fill="var(--orange-soft)"/>
    <polygon points="300,0 364,0 364,110" fill="var(--grey)"/>
    <rect x="35" y="40" width="165" height="110" fill="var(--photo-cool)" role="img" aria-label="Photo of hands working on a laptop"/>
    <rect x="65" y="40" width="40" height="72" fill="var(--orange)" opacity=".8"/>
    <rect x="130" y="112" width="52" height="38" fill="var(--navy)" opacity=".85"/>
  </svg>
  <div class="abs brand brand-sm" style="left:10px;top:190px"><i></i>Linden Peak</div>
  <div class="abs head" style="right:20px;top:22px;font-size:15px;text-align:right">Wealth<br><span class="hl" style="font-size:11px;letter-spacing:2px">Management</span></div>
  <div class="abs pill" style="right:20px;top:75px;width:52px;height:13px;line-height:13px;background:var(--orange);color:var(--white);font-size:6px;letter-spacing:1.5px">ABOUT US</div>
  <p class="abs body" style="left:232px;top:100px;width:120px;font-size:5.3px;text-align:justify">At <b>Linden Peak Wealth</b>, we are an independent firm of fiduciary investment advisors providing retirement planning and private wealth management for those preparing for and/or in retirement. Our firm is dedicated to making a difference in the lives of our clients, which is based on almost two decades worth of wealth management experience.</p>
</section>

<!-- Slide 6: services -->
<section class="slide" style="left:811px;top:288px">
  <svg class="bg" viewBox="0 0 364 210">
    <rect width="364" height="210" fill="#f4f4f6"/>
    <polygon points="150,0 364,0 364,210 190,210" fill="var(--white)"/>
    <polygon points="155,0 245,0 300,210 190,210" fill="var(--slate)"/>
    <g fill="var(--navy)">
      <path d="M48 46a24 24 0 0 1 24 24c0 16-24 36-24 36s-24-20-24-36a24 24 0 0 1 24-24z"/>
      <path d="M135 46a24 24 0 0 1 24 24c0 16-24 36-24 36s-24-20-24-36a24 24 0 0 1 24-24z"/>
      <path d="M222 46a24 24 0 0 1 24 24c0 16-24 36-24 36s-24-20-24-36a24 24 0 0 1 24-24z"/>
      <path d="M309 46a24 24 0 0 1 24 24c0 16-24 36-24 36s-24-20-24-36a24 24 0 0 1 24-24z"/>
    </g>
    <g fill="none" stroke="var(--orange)" stroke-width="1.5">
      <rect x="36" y="62" width="22" height="13" rx="1"/><circle cx="47" cy="68.5" r="3"/><rect x="52" y="70" width="10" height="9" rx="1" fill="var(--navy)"/>
      <circle cx="130" cy="69" r="7"/><circle cx="140" cy="69" r="7"/>
      <rect x="214" y="58" width="16" height="22" rx="1"/><line x1="218" y1="65" x2="226" y2="65"/><line x1="218" y1="70" x2="226" y2="70"/><line x1="218" y1="75" x2="223" y2="75"/>
      <circle cx="309" cy="69" r="9"/><path d="M309 60v9h9"/>
    </g>
  </svg>
  <div class="abs brand brand-sm" style="right:8px;top:12px"><i></i>Linden Peak</div>
  <div class="abs head" style="left:20px;top:12px;font-size:15px"><span class="hl">Our</span> Services</div>
  <div class="abs service" style="left:11px;top:108px"><h5>Money Management<br>Strategies</h5><p>Our unique and proprietary <b>money management methodology</b> combines cutting edge technology with diversification, so you have the money you need for the lifestyle you want. Our tactical strategies can be used alone or with other styles.</p></div>
  <div class="abs service" style="left:98px;top:108px"><h5>Business Retirement<br>Solutions</h5><p>Understanding the options available to businesses may help you <b>save</b> for retirement and lower your taxes. But what type of plan is right for your business? Some plans suit sole owners, while others fit firms with more than 10 staff.</p></div>
  <div class="abs service" style="left:185px;top:108px;color:var(--white)"><h5>Debt Freedom<br>Solutions</h5><p style="color:var(--white)">These solutions were created and offered for the client that wants to be shown just how much <b>Linden Peak</b> can save. We understand that sometimes you have to earn trust before you receive trust.</p></div>
  <div class="abs service" style="left:272px;top:108px"><h5>Personal Financial<br>Consultant</h5><p>The world of finance can be overwhelming at times. We offer just the support to bring it into focus one step at a time. This is exactly why we offer our expertise in the world of finance. We help educate, plan and build a '<b>Linden Peak Wealth Plan</b>' for our clients.</p></div>
</section>

<!-- Slide 7: insurance -->
<section class="slide" style="left:25px;top:513px">
  <svg class="bg" viewBox="0 0 364 210">
    <rect width="364" height="210" fill="var(--white)"/>
    <polygon points="0,0 90,0 0,60" fill="var(--grey)"/>
    <polygon points="175,0 320,0 290,210 130,210" fill="var(--slate)" opacity=".75"/>
    <polygon points="300,0 364,0 364,210 320,210" fill="var(--grey)"/>
    <rect x="165" y="22" width="153" height="150" fill="#8a7a63" role="img" aria-label="Close-up photo of a lion"/>
    <rect x="280" y="50" width="38" height="35" fill="var(--navy)" opacity=".9"/>
    <rect x="165" y="118" width="58" height="25" fill="var(--orange)" opacity=".9"/>
  </svg>
  <div class="abs brand brand-sm" style="left:15px;top:10px"><i></i>Linden Peak</div>
  <div class="abs head" style="right:214px;top:32px;font-size:16px;text-align:right"><span class="hl">Insurance</span><br><span style="font-size:12px">Management</span></div>
  <p class="abs body" style="left:20px;top:116px;width:128px;font-size:5.5px;text-align:justify">From growing wealth, to enjoying your retirement <b>Linden Peak Wealth</b> has custom created insurance strategies and solutions that will make the most out of your time and money. Explore which insurance based strategies and solutions are right for you.</p>
</section>

<!-- Slide 8: three pictures -->
<section class="slide" style="left:418px;top:513px">
  <svg class="bg" viewBox="0 0 364 210">
    <rect width="364" height="210" fill="var(--white)"/>
    <polygon points="0,0 150,0 0,120" fill="#f4f4f6"/>
    <polygon points="210,0 364,0 364,210 160,210" fill="var(--grey)"/>
    <rect x="155" y="52" width="62" height="70" fill="var(--photo-cool)" role="img" aria-label="Photo of an office discussion"/>
    <rect x="155" y="52" width="62" height="14" fill="var(--orange)" opacity=".85"/>
    <rect x="205" y="90" width="60" height="88" fill="var(--navy)" opacity=".9"/>
    <rect x="258" y="65" width="80" height="80" fill="#b8b6a8" role="img" aria-label="Photo of a businesswoman"/>
    <rect x="205" y="88" width="76" height="76" fill="#9fa3a7" role="img" aria-label="Photo of colleagues at a laptop"/>
    <rect x="295" y="128" width="43" height="17" fill="var(--orange)" opacity=".85"/>
    <rect x="227" y="136" width="30" height="28" fill="var(--navy)" opacity=".85"/>
  </svg>
  <div class="abs brand brand-sm" style="right:8px;top:194px"><i></i>Linden Peak</div>
  <div class="abs head" style="left:18px;top:30px;font-size:15px"><span class="hl">Three Pictures</span><br><span style="font-size:12px">Slide</span></div>
  <p class="abs body" style="left:18px;top:118px;width:135px">Lorem ipsum dolor sit amet, qui te sint sanctus, et his vero zril reprimique. Eu eos inani percipit laboramus. Sed te labitur abhorreant constituam, purto diceret mei cu. Wisi luptatum no nam, adhuc graeci accusata ne nec. Modo saperet pertinax sea ei, dicit eirmod torquatos pro at, mei soluta diceret contentiones eu. No sea nobis antiopam.</p>
</section>

<!-- Slide 9: data table -->
<section class="slide" style="left:811px;top:513px">
  <svg class="bg" viewBox="0 0 364 210">
    <defs><linearGradient id="dataBg" x1="0" y1="0" x2="1" y2="1"><stop offset="0" stop-color="#3e4b68"/><stop offset="1" stop-color="var(--navy-deep)"/></linearGradient></defs>
    <rect width="364" height="210" fill="url(#dataBg)" role="img" aria-label="Faint office photo behind navy overlay"/>
  </svg>
  <div class="abs head" style="left:0;width:364px;top:16px;font-size:16px;text-align:center;color:var(--white)">Data <span class="hl">Slides</span></div>
  <div class="abs pill" style="left:130px;top:52px;width:104px;height:14px;line-height:14px;background:var(--navy-deep);color:var(--orange);font-size:6px">Lorem ipsum dolor sit amet</div>
  <table class="abs data" style="left:62px;top:84px;width:240px">
    <tr><th>No</th><th>Categories</th><th>Staff 1</th><th>Staff 2</th><th>Staff 3</th></tr>
    <tr><td>1</td><td>Lorem ipsum</td><td>132</td><td>276</td><td>254</td></tr>
    <tr><td>2</td><td>Dolor sin</td><td>456</td><td>895</td><td>573</td></tr>
    <tr><td>3</td><td>Eu eos inani</td><td>2345</td><td>625</td><td>537</td></tr>
    <tr><td>4</td><td>Modo saperet pertinax</td><td>756</td><td>324</td><td>247</td></tr>
  </table>
  <p class="abs" style="left:102px;top:155px;width:160px;font-size:5.5px;line-height:1.45;color:#c9ccd6;text-align:center">Wisi luptatum no nam, adhuc graeci accusata ne nec. Modo saperet pertinax sea ei, dicit eirmod torquatos pro at, mei soluta diceret contentiones eu. No sea nobis antiopam.</p>
</section>

<!-- Slide 10: bar chart -->
<section class="slide" style="left:25px;top:738px">
  <svg class="bg" viewBox="0 0 364 210">
    <rect width="364" height="210" fill="var(--white)"/>
    <polygon points="140,0 275,0 330,210 178,210" fill="var(--orange-soft)"/>
    <polygon points="275,0 364,0 364,210 330,210" fill="#f4f4f6"/>
    <rect x="10" y="72" width="170" height="120" fill="var(--white)"/>
    <g font-family="Open Sans, sans-serif" font-size="3.5" fill="#777">
      <rect x="55" y="78" width="4" height="3" fill="var(--navy)"/><text x="61" y="81">Series 1</text>
      <rect x="80" y="78" width="4" height="3" fill="var(--orange)"/><text x="86" y="81">Series 2</text>
      <rect x="105" y="78" width="4" height="3" fill="#c8c8cc"/><text x="111" y="81">Series 3</text>
    </g>
    <line x1="14" y1="180" x2="176" y2="180" stroke="#ccc" stroke-width=".6"/>
    <g>
      <rect x="24" y="114.4" width="6" height="65.6" fill="var(--navy)"/><rect x="32" y="143.4" width="6" height="36.6" fill="var(--orange)"/><rect x="40" y="149.5" width="6" height="30.5" fill="#c8c8cc"/>
      <rect x="64" y="141.9" width="6" height="38.1" fill="var(--navy)"/><rect x="72" y="112.9" width="6" height="67.1" fill="var(--orange)"/><rect x="80" y="149.5" width="6" height="30.5" fill="#c8c8cc"/>
      <rect x="104" y="126.6" width="6" height="53.4" fill="var(--navy)"/><rect x="112" y="152.5" width="6" height="27.5" fill="var(--orange)"/><rect x="120" y="134.2" width="6" height="45.8" fill="#c8c8cc"/>
      <rect x="144" y="111.4" width="6" height="68.6" fill="var(--navy)"/><rect x="152" y="137.3" width="6" height="42.7" fill="var(--orange)"/><rect x="160" y="103.8" width="6" height="76.2" fill="#c8c8cc"/>
    </g>
    <g font-family="Open Sans, sans-serif" font-size="3.5" fill="#555" text-anchor="middle">
      <text x="35" y="188">CATEGORY 1</text><text x="75" y="188">CATEGORY 2</text><text x="115" y="188">CATEGORY 3</text><text x="155" y="188">CATEGORY 4</text>
      <text x="27" y="112">4.3</text><text x="35" y="141">2.4</text><text x="43" y="147">2</text>
      <text x="67" y="139">2.5</text><text x="75" y="110">4.4</text><text x="83" y="147">2</text>
      <text x="107" y="124">3.5</text><text x="115" y="150">1.8</text><text x="123" y="132">3</text>
      <text x="147" y="109">4.5</text><text x="155" y="135">2.8</text><text x="163" y="101">5</text>
    </g>
  </svg>
  <div class="abs brand brand-sm" style="right:8px;top:10px"><i></i>Linden Peak</div>
  <div class="abs head" style="left:18px;top:12px;font-size:15px">Chart <span class="hl">Slides</span></div>
  <div class="abs" style="left:18px;top:40px;font-size:5.8px;color:var(--navy)">Lorem ipsum dolor sit amet, cui te sint sanctus, et his vero zril repemique.</div>
  <div class="abs" style="left:60px;top:64px;font-size:6px;font-weight:700;color:var(--navy)">CHART TITLE</div>
  <p class="abs body" style="left:244px;top:94px;width:110px;text-align:justify">Lorem ipsum dolor sit amet, qui te sint sanctus, et his vero zril reprimique. Eu eos inani percipit laboramus. Sed te labitur abhorreant constituam, purto diceret mei cu. Wisi luptatum no nam, adhuc graeci accusata ne nec. Modo saperet pertinax sea ei, dicit eirmod torquatos pro at, mei soluta diceret contentiones eu. No sea nobis antiopam.</p>
</section>

<!-- Slide 11: pie chart -->
<section class="slide" style="left:418px;top:738px">
  <svg class="bg" viewBox="0 0 364 210">
    <rect width="364" height="210" fill="var(--white)"/>
    <rect width="182" height="210" fill="var(--navy)" role="img" aria-label="Faint financial documents photo behind navy overlay"/>
    <g font-family="Open Sans, sans-serif" font-size="3.5" fill="#dfe3ec">
      <rect x="32" y="32" width="3" height="3" fill="var(--navy-deep)" stroke="#fff" stroke-width=".3"/><text x="37" y="35">1st Qtr</text>
      <rect x="58" y="32" width="3" height="3" fill="var(--orange)"/><text x="63" y="35">2nd Qtr</text>
      <rect x="85" y="32" width="3" height="3" fill="var(--blue)"/><text x="90" y="35">3rd Qtr</text>
      <rect x="110" y="32" width="3" height="3" fill="var(--orange-soft)"/><text x="115" y="35">4th Qtr</text>
    </g>
    <g transform="translate(88 120)" stroke="var(--white)" stroke-width=".8">
      <path d="M0 0L0 -55A55 55 0 1 1 -26.5 48.2Z" fill="var(--navy-deep)"/>
      <path d="M0 0L-26.5 48.2A55 55 0 0 1 -51.1 -20.2Z" fill="var(--orange-soft)"/>
      <path d="M0 0L-51.1 -20.2A55 55 0 0 1 -29.5 -46.4Z" fill="var(--blue)"/>
      <path d="M0 0L-29.5 -46.4A55 55 0 0 1 0 -55Z" fill="var(--orange)"/>
    </g>
    <g font-family="Open Sans, sans-serif" font-size="4.5" font-weight="600" fill="#fff" text-anchor="middle">
      <text x="120" y="125">1st Qtr</text><text x="120" y="131">58%</text>
      <text x="60" y="145">2nd Qtr</text><text x="60" y="151">23%</text>
      <text x="48" y="102">3rd Qtr</text><text x="48" y="108">10%</text>
      <text x="73" y="80">4th Qtr</text><text x="73" y="86">9%</text>
    </g>
    <line x1="198" y1="120" x2="348" y2="120" stroke="#bbb" stroke-width=".6"/>
  </svg>
  <div class="abs head" style="left:72px;top:18px;font-size:6px;color:var(--white)">Sales</div>
  <div class="abs brand brand-sm" style="left:18px;top:10px;color:var(--white)"><i></i>Linden Peak</div>
  <div class="abs head" style="right:14px;top:14px;font-size:15px">Chart <span class="hl">Slides</span></div>
  <div class="abs" style="left:198px;top:44px;font-size:5.8px;color:var(--navy)">Lorem ipsum dolor sit amet, qui te sint sanctus.</div>
  <p class="abs body" style="left:198px;top:78px;width:150px">Wisi luptatum no nam, adhuc graeci accusata ne nec. Modo saperet pertinax sea ei, dicit eirmod torquatos pro at, mei soluta diceret contentiones eu. No sea nobis antiopam.</p>
  <p class="abs body" style="left:198px;top:132px;width:150px">Lorem ipsum dolor sit amet, qui te sint sanctus, et his vero zril reprimique. Eu eos inani percipit laboramus. Sed te labitur abhorreant constituam, purto diceret mei cu. Wisi luptatum no nam, adhuc graeci accusata ne nec. Modo saperet pertinax sea ei, dicit eirmod torquatos pro at, mei soluta diceret contentiones eu. No sea nobis antiopam.</p>
</section>

<!-- Slide 12: closing -->
<section class="slide" style="left:811px;top:738px">
  <svg class="bg" viewBox="0 0 364 210">
    <rect width="364" height="210" fill="var(--grey)"/>
    <polygon points="0,0 70,0 0,60" fill="#f4f4f6"/>
    <polygon points="170,0 364,0 364,210 200,210" fill="var(--photo-warm)" role="img" aria-label="Photo of a desk with financial papers"/>
    <polygon points="110,0 210,0 200,210 150,210" fill="var(--white)" opacity=".5"/>
    <rect x="218" y="0" width="55" height="102" fill="var(--orange)" opacity=".85"/>
    <rect x="268" y="122" width="96" height="58" fill="var(--navy)" opacity=".9"/>
    <polygon points="0,196 120,196 110,210 0,210" fill="var(--blue)"/>
    <polygon points="255,196 364,196 364,210 247,210" fill="var(--orange)"/>
  </svg>
  <div class="abs brand" style="left:18px;top:30px;font-size:9px"><i style="width:12px;height:12px"></i>Linden Peak</div>
  <div class="abs dots" style="left:20px;top:86px">
    <b style="background:var(--navy)"></b><b style="background:var(--blue)"></b><b style="background:var(--blue)"></b><b style="background:var(--orange)"></b><b style="background:var(--orange)"></b><b style="background:var(--grey-mid)"></b>
  </div>
  <div class="abs contact" style="left:20px;top:104px">
    <h4>CONTACT INFORMATION</h4>
    <a>Toll Free: 1.800.555.0147</a>
    <a>info@LindenPeak.com</a>
  </div>
  <div class="abs" style="left:20px;top:172px;font-size:6.5px;font-style:italic;color:#444">http://lindenpr.kzqt4-rv7.b9servo.com/</div>
</section>

</body>
</html>
```